Business card, Invoice and printable service brochure

I need a 5.5x8.5 invoice, business card and printable service template for reception desk designed for my Rug repair, restoration and cleaning business.

I have included a picture for reference

www.belkarrug.com

Columns i need in my invoice:
Type of rug, Size, Background Color, Repair needs, Notes, Price and rug cleaning disclaimer.

Target Market(s)

Higher segment clients

Industry/Entity Type

Rug Repair, Restoration and cleaning,

Requirements
Must have
• Services hast to be listed on the invoice as well as service brochure.

```html
<!DOCTYPE html>
<html lang="en">
<head>
<meta charset="UTF-8">
<title>Belkar Rug — Business Card</title>
<link rel="stylesheet" href="https://fonts.googleapis.com/css2?family=Marcellus&family=Libre+Baskerville&display=swap">
<style>
  :root {
    --backdrop: #d9c4a1;
    --card-black: #0b0a09;
    --pattern-dark: #1c1812;
    --pattern-mid: #2a2318;
    --gold: #c29a4e;
    --gold-bright: #d4a93c;
    --ink-light: #ece6da;
    --rug-deep: #1b120b;
    --rug-ochre: #b7852f;
    --rug-coral: #c9573a;
  }
  * { margin: 0; padding: 0; box-sizing: border-box; }
  html, body {
    width: 1200px; height: 1200px; overflow: hidden;
    background: var(--backdrop);
  }
  .sheet {
    width: 1200px; height: 1200px;
    display: flex; flex-direction: column; align-items: center; justify-content: center;
    gap: 60px;
  }
  .card {
    position: relative;
    width: 840px; height: 480px;
    background: var(--card-black);
    overflow: hidden;
    box-shadow: 0 14px 30px rgba(60, 40, 15, 0.25);
  }

  /* Front */
  .card-front .pattern-field {
    position: absolute; inset: 0;
    background: radial-gradient(ellipse at center, var(--card-black) 0%, var(--card-black) 38%, var(--pattern-mid) 75%, var(--pattern-dark) 100%);
  }
  .brand-lockup {
    position: absolute; left: 50%; top: 50%;
    transform: translate(-50%, -50%);
    width: 680px;
    display: flex; flex-direction: column; align-items: center;
  }
  .rule { display: block; height: 3px; background: var(--gold); }
  .rule-top { width: 250px; margin-bottom: 24px; }
  .rule-bottom { width: 250px; margin-top: 24px; }
  .brand-name {
    font-family: "Marcellus", serif;
    font-weight: 400;
    font-size: 84px; line-height: 1;
    letter-spacing: 2px;
    color: var(--gold);
  }
  .brand-services {
    margin-top: 10px;
    font-family: "Marcellus", serif;
    font-size: 18px;
    letter-spacing: 8px;
    color: var(--gold);
    white-space: nowrap;
  }

  /* Back */
  .card-back { display: flex; }
  .rug-panel {
    width: 226px; height: 100%;
    background:
      radial-gradient(circle at 30% 20%, var(--rug-coral) 0%, transparent 35%),
      radial-gradient(circle at 70% 60%, var(--rug-ochre) 0%, transparent 40%),
      radial-gradient(circle at 35% 85%, var(--rug-coral) 0%, transparent 30%),
      linear-gradient(160deg, var(--rug-ochre), var(--rug-deep) 55%, var(--rug-ochre));
  }
  .contact-panel { position: relative; flex: 1; }
  .contact-panel .pattern-band {
    position: absolute; left: 0; right: 0; top: 0; height: 150px;
    background: linear-gradient(180deg, var(--pattern-mid), var(--card-black));
  }
  .contact-body {
    position: relative;
    padding: 44px 44px 0 40px;
  }
  .contact-name {
    font-family: "Libre Baskerville", serif;
    font-weight: 400;
    font-size: 48px; line-height: 0.92;
    letter-spacing: 1px;
    color: var(--gold-bright);
    margin: 0 0 26px 4px;
  }
  .contact-list { list-style: none; }
  .contact-item {
    font-family: "Libre Baskerville", serif;
    font-weight: 400;
    font-size: 22px;
    letter-spacing: 0.5px;
    color: var(--ink-light);
    border-top: 1.5px solid var(--gold);
    padding: 14px 0 16px 6px;
    line-height: 1.5;
  }
  .contact-item:last-child { border-bottom: 1.5px solid var(--gold); }
</style>
</head>
<body>
<main class="sheet">
  <section class="card card-front" aria-label="Business card front">
    <div class="pattern-field" role="img" aria-label="Dark ornamental floral rosette pattern"></div>
    <div class="brand-lockup">
      <span class="rule rule-top"></span>
      <h1 class="brand-name">BELKAR RUG</h1>
      <p class="brand-services">REPAIR | RESTORATION | CLEANING</p>
      <span class="rule rule-bottom"></span>
    </div>
  </section>

  <section class="card card-back" aria-label="Business card back">
    <div class="rug-panel" role="img" aria-label="Close-up of a hand-knotted rug with coral and ochre florals on black"></div>
    <div class="contact-panel">
      <div class="pattern-band" role="img" aria-label="Dark ornamental floral rosette pattern"></div>
      <div class="contact-body">
        <h2 class="contact-name">Belkar<br>Rug</h2>
        <ul class="contact-list">
          <li class="contact-item">(555)014-2260</li>
          <li class="contact-item">info@belkarrug.com</li>
          <li class="contact-item">1480 Marlow Ave, Fairbrook, IL<br>60990</li>
        </ul>
      </div>
    </div>
  </section>
</main>
</body>
</html>
```